Home Security Company Business Card

Looking for a eye catching business card that is non traditional and stands out but yet still looks professional. It should include all the pertinent information such as name, title, address, telephone, e-mail, website address should definitely stand out and then finally the logo.

Target Market(s)

Residential and Commercial accounts mostly upscale accounts

Industry/Entity Type

Security

Contact Information for Business Card

Name
Title
Address
Office #
Cell #
E-mail
Website

Font styles to use
Serif
Sans Serif

Requirements
Must have
• Logo, two sided color configuration
Nice to have
• You decide
Should not have
• There really aren't any.

```html
<!DOCTYPE html>
<html lang="en">
<head>
<meta charset="utf-8">
<title>Harborline Protection Group – Business Card</title>
<link rel="stylesheet" href="https://fonts.googleapis.com/css2?family=Libre+Baskerville&family=Open+Sans:wght@400;600;700&display=swap">
<style>
  :root {
    --backdrop: #c8ddd2;
    --card: #ffffff;
    --maroon: #7a1510;
    --gold: #e2a72c;
    --gold-light: #f6e3a0;
    --copper: #c0611f;
    --rust: #a8250f;
    --ink: #1c1c1c;
  }
  * { box-sizing: border-box; margin: 0; padding: 0; }
  html, body {
    width: 1200px;
    height: 1000px;
    overflow: hidden;
    background: var(--backdrop);
  }
  .canvas { position: relative; width: 1200px; height: 1000px; }

  .card {
    position: absolute;
    background: var(--card);
    border-radius: 34px;
    overflow: hidden;
    box-shadow: 0 10px 26px rgba(40, 70, 60, 0.18);
  }
  .card-back  { left: 600px; top: 120px; width: 480px; height: 274px; }
  .card-front { left: 120px; top: 500px; width: 600px; height: 342px; }

  .accent-band {
    position: absolute;
    left: 0; right: 0; bottom: 0;
    height: 13%;
    background: linear-gradient(90deg,
      var(--copper) 0%, var(--gold) 22%, var(--gold-light) 42%,
      var(--gold) 52%, var(--copper) 68%, var(--rust) 82%, var(--maroon) 100%);
  }

  .brand-mark {
    position: absolute;
    border-radius: 50%;
    background: var(--maroon);
  }
  .brand-name {
    font-family: "Libre Baskerville", serif;
    font-weight: 400;
    color: var(--maroon);
    text-transform: uppercase;
    line-height: 1;
  }
  .brand-name .line-sub { display: block; font-size: 0.45em; margin-top: 2px; letter-spacing: 0.02em; }

  /* back */
  .card-back .brand-mark { left: 130px; top: 70px; width: 100px; height: 100px; }
  .card-back .brand-name { position: absolute; left: 244px; top: 102px; font-size: 20px; }

  /* front */
  .card-front .brand-mark { left: 70px; top: 72px; width: 170px; height: 170px; }
  .contact-block {
    position: absolute;
    left: 270px; top: 44px; width: 290px;
    font-family: "Open Sans", sans-serif;
  }
  .contact-block .brand-name { font-size: 27px; margin-bottom: 6px; }
  .person-name { color: var(--gold); font-weight: 700; font-size: 19px; letter-spacing: 0.03em; line-height: 1.1; }
  .person-title { color: var(--gold); font-weight: 400; font-size: 17px; letter-spacing: 0.08em; padding-left: 96px; line-height: 1.1; }
  .phone { color: var(--ink); font-weight: 700; font-size: 20px; letter-spacing: 0.08em; padding-left: 70px; line-height: 1.2; }
  .email, .website { color: var(--maroon); font-weight: 600; font-size: 14.5px; line-height: 1.3; }
  .email { padding-left: 40px; }
  .address { color: var(--gold); font-size: 13px; text-align: right; line-height: 1.25; padding-right: 6px; }
</style>
</head>
<body>
<div class="canvas">

  <section class="card card-back" aria-label="Business card back">
    <span class="brand-mark"></span>
    <p class="brand-name">Harborline<span class="line-sub">Protection Group Inc.</span></p>
    <div class="accent-band"></div>
  </section>

  <section class="card card-front" aria-label="Business card front">
    <span class="brand-mark"></span>
    <div class="contact-block">
      <p class="brand-name">Harborline<span class="line-sub">Protection Group Inc.</span></p>
      <p class="person-name">NAME SURNAME</p>
      <p class="person-title">TITLE TITLE</p>
      <p class="phone">1234 5678</p>
      <p class="email">info@harborlineprotect.com</p>
      <p class="website">www.harborlineprotect.com</p>
      <p class="address">Address 1234, Address 56<br>Office 78</p>
    </div>
    <div class="accent-band"></div>
  </section>

</div>
</body>
</html>
```